"Cork Hollow Excursions" is a top notch Santa Barbara County Wine Tour company.

We provide scenic, boutique and custom wine tours. I need the card to be clean and classy. I will provide our logo. I would like the logo to cover the back side of the card as an option and would like to see a couple color options other then our signature green and gold. I would like to see some creative options and let the designers come up with options.
I need cards for myself and my team. The final design should communicate "An authentic and boutique wine tour experience"
Please use my website for reference www.corkhollowexcursions.com

Target Market(s)

We have a wide range of clients from millennials to baby boomers

Industry/Entity Type

Tour

Contact Information for Business Card

Contact info:
Dale Munford
805-291-6384
info@corkhollowexcursions.com
corkhollowexcursions.com

Colors

Designer to choose colors to be used in the design.

Requirements
Must have
• my logo
Nice to have
• *I would like to have the backside side with the logo and the company statement
• "An authentic and boutique wine tour experience" as an option.
• *I would also like to see what the designers can create!
• *I would like to see an option that incorporates or social: snapgrid, rovia, route scout
Should not have
• I do not want it too busy.

```html
<!DOCTYPE html>
<html lang="en">
<head>
<meta charset="utf-8">
<title>Cork Hollow Excursions – Business Card</title>
<link rel="stylesheet" href="https://fonts.googleapis.com/css2?family=Cinzel:wght@400;500&family=Roboto:wght@400&family=Roboto+Condensed:wght@400&display=swap">
<style>
  :root {
    --backdrop: #ebe7e1;
    --card-white: #f4f4f4;
    --card-white-edge: #dcdcdc;
    --vine-green: #236843;
    --rule-green: #2f6b45;
    --gold: #9a8666;
    --gold-light: #b3a284;
    --ink: #4a4a4a;
  }
  * { margin: 0; padding: 0; box-sizing: border-box; }
  html, body { width: 1200px; height: 960px; overflow: hidden; }
  body { background: var(--backdrop); position: relative; }

  .card { position: absolute; box-shadow: 0 2px 6px rgba(0,0,0,.25); }

  .card-front {
    left: 302px; top: 129px; width: 600px; height: 343px;
    background: linear-gradient(90deg, #ffffff 0%, var(--card-white) 50%, var(--card-white-edge) 100%);
    text-align: center;
  }
  .brand-mark {
    position: absolute; left: 0; right: 0; top: 238px;
  }
  .front-brand {
    position: absolute; left: 0; right: 0; top: 248px;
    font-family: "Cinzel", serif; font-weight: 500; font-size: 26px;
    letter-spacing: 1px; color: var(--gold);
  }
  .front-brand-box {
    position: absolute; left: 0; right: 0; top: 36px; height: 150px;
    display: flex; align-items: center; justify-content: center; gap: 12px;
  }
  .front-brand-box .mark-square {
    width: 18px; height: 18px; background: var(--vine-green);
  }
  .front-brand-box .brand-name {
    font-family: "Cinzel", serif; font-weight: 500; font-size: 30px;
    color: var(--gold); letter-spacing: 1px;
  }
  .holder-name {
    position: absolute; left: 0; right: 0; top: 207px;
    font-family: "Cinzel", serif; font-weight: 500; font-size: 30px;
    color: var(--gold); letter-spacing: .5px;
  }
  .contact-line {
    position: absolute; left: 68px; width: 453px; top: 263px; height: 33px;
    border-top: 1px solid var(--rule-green); border-bottom: 1px solid var(--rule-green);
    display: flex; align-items: center; justify-content: center;
    font-family: "Roboto", sans-serif; font-size: 14.5px; color: var(--ink);
    white-space: nowrap;
  }

  .card-back {
    left: 299px; top: 488px; width: 600px; height: 343px;
    background: var(--vine-green);
    text-align: center;
  }
  .back-brand {
    position: absolute; left: 0; right: 0; top: 60px; height: 160px;
    display: flex; align-items: center; justify-content: center; gap: 14px;
  }
  .back-brand .mark-circle {
    width: 26px; height: 26px; border-radius: 50%; background: var(--gold-light);
  }
  .back-brand .brand-name {
    font-family: "Cinzel", serif; font-weight: 500; font-size: 34px;
    color: var(--gold-light); letter-spacing: 1px;
  }
  .tagline {
    position: absolute; left: 0; right: 0; top: 220px;
    font-family: "Roboto Condensed", sans-serif; font-size: 15px;
    color: var(--gold-light);
  }
  .social-row {
    position: absolute; left: 0; right: 0; top: 285px;
    display: flex; justify-content: center; gap: 14px;
    list-style: none;
  }
  .social-row li {
    display: flex; align-items: center; gap: 5px;
    font-family: "Roboto", sans-serif; font-size: 11px; color: #cfe3d5;
  }
  .social-row .dot {
    width: 12px; height: 12px; background: #6fa384; border-radius: 2px;
  }
</style>
</head>
<body>
  <section class="card card-front" aria-label="Business card front">
    <div class="front-brand-box">
      <span class="mark-square"></span>
      <span class="brand-name">Cork Hollow Excursions</span>
    </div>
    <h1 class="holder-name">Dale Munford</h1>
    <p class="contact-line">805-291-6384 | info@corkhollowexcursions.com | corkhollowexcursions.com</p>
  </section>

  <section class="card card-back" aria-label="Business card back">
    <div class="back-brand">
      <span class="mark-circle"></span>
      <span class="brand-name">Cork Hollow Excursions</span>
    </div>
    <p class="tagline">An authentic &amp; boutique wine tour experience</p>
    <ul class="social-row">
      <li><span class="dot"></span>route scout</li>
      <li><span class="dot"></span>friendwall</li>
      <li><span class="dot"></span>snapgrid</li>
      <li><span class="dot"></span>rovia</li>
      <li><span class="dot"></span>chirplet</li>
    </ul>
  </section>
</body>
</html>
```